Executive retreat/workshop flyer for Harbor Pathway

Our company, Harbor Pathway, runs intensive week long residential retreats for executives suffering from burnout syndrome. We have a programme of therapy which will enable clients to get clarity on what they want out of life and how to achieve it.

Our website is www.harborpathway-example.com. The flyer should have a consistent look and feel to the website. The flyer should be suitable for electronic distribution as well as printing.

The copy should read:

What is it all for? (IN BIG BOLD FONT)

We invite you to The Harbor Pathway

Discover a more meaningful way of being in this world and put passion and purpose back into your life.

Our leading experts will guide you through a holistic program of intellectual, physical, emotional, spiritual and financial work.

You will:

- Draw up a vision of how you want to live your life
- Understand negative behavior loops and how to manage them
- Rebalance relationships which have suffered from stress and neglect
- Examine your attitudes towards money through the Quadrafold System
- Access practical advice on how to implement your goals

Please join us in the beautiful Castlereagh Peninsula this August for a life-changing journey.

This is an intensive program custom tailored to your individual needs. We can only take on a very limited number of participants to maintain intimacy and quality of attention. Book early to avoid disappointment.

Details:

date - mon 27 August - sat 1 sept 2012

Venue- kestrelwood Eco retreat, stony ford, Australia, 1 hour from Melbourne

Price- Special launch offer of US$ 13,860 which is a 30% discount off the normal price of US$ 19,800

10% of profits go to charity

All accommodation, food and individual consultations included.

Please email info@harborpathway-example.com or contact Marnie at 6031 2946

Target Market(s)

Senior executives and leaders mostly with a financial background.

Industry/Entity Type

Residential

Requirements
Must have
• The brochure should look clear in electronic and print format. Can use photos which I've attached.
Nice to have
• Should have a warm, serene feel but appear professional and reliable.

```html
<!DOCTYPE html>
<html lang="en">
<head>
<meta charset="utf-8">
<title>The Harbor Pathway – Retreat Invitation</title>
<link rel="stylesheet" href="https://fonts.googleapis.com/css2?family=Cinzel:wght@400;500&family=Montserrat:wght@400;700&display=swap">
<style>
  :root {
    --olive: #6f6d1d;
    --olive-deep: #55530f;
    --olive-light: #8a8a2c;
    --header-bg: #e9ebee;
    --purple: #5f1a63;
    --purple-soft: #7d2d80;
    --white: #ffffff;
    --gold: #f3c21c;
    --amber: #f0a821;
    --cta: #f7d320;
  }
  * { margin: 0; padding: 0; box-sizing: border-box; }
  html, body { width: 848px; height: 1200px; overflow: hidden; background: var(--olive); }
  .flyer {
    position: relative; width: 848px; height: 1200px; overflow: hidden;
    font-family: "Montserrat", Arial, sans-serif; color: var(--white);
  }
  .backdrop {
    position: absolute; inset: 0;
    background:
      radial-gradient(circle at 90% 20%, rgba(255,255,230,.55), transparent 18%),
      radial-gradient(ellipse at 20% 75%, rgba(180,180,60,.35), transparent 40%),
      linear-gradient(180deg, #7f8a2a 0%, #6f6d1d 30%, #5d5b14 60%, #7a7a26 80%, #6a6819 100%);
  }
  .header-band {
    position: absolute; left: 0; top: 43px; width: 848px; height: 263px;
    background: linear-gradient(180deg, rgba(240,242,245,.96), rgba(226,230,234,.94));
  }
  .invite-line {
    position: absolute; left: 60px; top: 128px;
    font-family: "Cinzel", Georgia, serif; font-size: 27px; letter-spacing: 6px;
    color: var(--purple-soft);
  }
  .event-title {
    position: absolute; left: 58px; top: 158px;
    font-family: "Cinzel", Georgia, serif; font-weight: 400; font-size: 66px;
    color: var(--purple); letter-spacing: 1px; white-space: nowrap;
  }
  .intro { position: absolute; left: 72px; top: 340px; width: 720px; list-style: none; }
  .intro li {
    position: relative; padding-left: 44px; margin-bottom: 14px;
    font-weight: 700; font-size: 18.5px; line-height: 1.35;
  }
  .intro svg { position: absolute; left: 0; top: 2px; }
  .section-title {
    position: absolute; left: 62px; top: 478px;
    font-family: "Cinzel", Georgia, serif; font-size: 44px; color: var(--purple-soft);
  }
  .outcomes { position: absolute; left: 86px; top: 538px; list-style: none; }
  .outcomes li {
    position: relative; padding-left: 30px; height: 26px;
    font-weight: 700; font-size: 17px; line-height: 26px;
  }
  .outcomes svg { position: absolute; left: 0; top: 5px; }
  .copy { position: absolute; left: 82px; width: 700px; font-size: 19px; line-height: 1.4; }
  .copy-join { top: 727px; }
  .copy-program { top: 806px; }
  .details-band {
    position: absolute; left: 0; top: 898px; width: 848px; height: 182px;
    background: linear-gradient(180deg, rgba(150,150,50,.35), rgba(120,120,40,.25));
  }
  .detail {
    position: absolute; top: 924px; width: 260px; text-align: center;
    font-weight: 700; font-size: 16.5px; line-height: 1.3;
  }
  .detail svg { display: block; margin: 0 auto 12px; }
  .detail-date { left: 12px; }
  .detail-venue { left: 294px; }
  .detail-price { left: 570px; }
  .footer { position: absolute; left: 0; top: 1090px; width: 848px; text-align: center; font-size: 17px; line-height: 1.35; }
  .footer .cta { color: var(--cta); font-weight: 700; margin-top: 4px; }
</style>
</head>
<body>
<div class="flyer">
  <div class="backdrop" role="img" aria-label="Soft-focus photograph of green foliage with warm sunlight and bokeh"></div>

  <div class="header-band"></div>
  <p class="invite-line">WE INVITE YOU TO</p>
  <h1 class="event-title">THE HARBOR PATHWAY</h1>

  <ul class="intro">
    <li><svg width="32" height="32" viewBox="0 0 32 32"><circle cx="16" cy="16" r="16" fill="var(--amber)"/><path d="M9 24 C9 14 15 8 24 8 C24 17 18 23 9 24 Z" fill="#fff4c8"/></svg>Discover a more meaningful way of being in this world and put passion and purpose back into your life.</li>
    <li><svg width="32" height="32" viewBox="0 0 32 32"><circle cx="16" cy="16" r="16" fill="var(--amber)"/><path d="M9 24 C9 14 15 8 24 8 C24 17 18 23 9 24 Z" fill="#fff4c8"/></svg>Our leading experts will guide you through a holistic program of intellectual, physical, emotional, spiritual and financial work.</li>
  </ul>

  <h2 class="section-title">YOU WILL</h2>
  <ul class="outcomes">
    <li><svg width="17" height="17" viewBox="0 0 24 24"><path d="M12 1l3.2 7 7.6.8-5.7 5.1 1.6 7.5L12 17.6 5.3 21.4l1.6-7.5L1.2 8.8 8.8 8z" fill="var(--gold)"/></svg>Draw up a vision of how you want to live your life</li>
    <li><svg width="17" height="17" viewBox="0 0 24 24"><path d="M12 1l3.2 7 7.6.8-5.7 5.1 1.6 7.5L12 17.6 5.3 21.4l1.6-7.5L1.2 8.8 8.8 8z" fill="var(--gold)"/></svg>Understand negative behavior loops and how to manage them</li>
    <li><svg width="17" height="17" viewBox="0 0 24 24"><path d="M12 1l3.2 7 7.6.8-5.7 5.1 1.6 7.5L12 17.6 5.3 21.4l1.6-7.5L1.2 8.8 8.8 8z" fill="var(--gold)"/></svg>Examine your attitudes towards money through the Quadrafold System</li>
    <li><svg width="17" height="17" viewBox="0 0 24 24"><path d="M12 1l3.2 7 7.6.8-5.7 5.1 1.6 7.5L12 17.6 5.3 21.4l1.6-7.5L1.2 8.8 8.8 8z" fill="var(--gold)"/></svg>Access practical advice on how to implement your goals</li>
    <li><svg width="17" height="17" viewBox="0 0 24 24"><path d="M12 1l3.2 7 7.6.8-5.7 5.1 1.6 7.5L12 17.6 5.3 21.4l1.6-7.5L1.2 8.8 8.8 8z" fill="var(--gold)"/></svg>Rebalance relationships which have suffered from stress and neglect</li>
  </ul>

  <p class="copy copy-join">Please join us in the beautiful Castlereagh Peninsula this August for a life-changing journey.</p>
  <p class="copy copy-program">This is an intensive program custom tailored to your individual needs. We can only take on a very limited number of participants to maintain intimacy and quality of attention. Book early to avoid disappointment.</p>

  <div class="details-band"></div>
  <div class="detail detail-date">
    <svg width="48" height="48" viewBox="0 0 48 48"><rect x="3" y="8" width="42" height="37" rx="3" fill="none" stroke="var(--amber)" stroke-width="3"/><rect x="3" y="8" width="42" height="9" fill="var(--amber)"/><rect x="12" y="3" width="4" height="10" rx="2" fill="var(--amber)"/><rect x="32" y="3" width="4" height="10" rx="2" fill="var(--amber)"/><text x="24" y="38" text-anchor="middle" font-family="Montserrat, Arial, sans-serif" font-size="16" font-weight="700" fill="var(--amber)">23</text></svg>
    Monday, 27 August<br>though<br>Saturday, 1 September 2012
  </div>
  <div class="detail detail-venue">
    <svg width="48" height="48" viewBox="0 0 48 48"><path d="M24 3C15 3 9 10 9 18c0 11 15 27 15 27s15-16 15-27C39 10 33 3 24 3z" fill="var(--amber)"/><circle cx="24" cy="18" r="6" fill="var(--olive)"/></svg>
    Kestrelwood Eco Retreat<br>Stony Ford, Australia<br>1 hour from Melbourne
  </div>
  <div class="detail detail-price">
    <svg width="48" height="48" viewBox="0 0 48 48"><path d="M18 5h12l-3 7h-6z" fill="var(--amber)"/><path d="M20 13h8c8 6 13 14 13 21 0 7-6 11-17 11S7 41 7 34c0-7 5-15 13-21z" fill="var(--amber)"/><text x="24" y="38" text-anchor="middle" font-family="Montserrat, Arial, sans-serif" font-size="16" font-weight="700" fill="var(--olive)">$</text></svg>
    Special launch offer of<br>$13,860 US. A 30% discount<br>off the normal price<br>of $19,800 US
  </div>

  <div class="footer">
    <p>10% of profits go to charity</p>
    <p>All accommodation, food and individual consultations included.</p>
    <p class="cta">Please email info@harborpathway-example.com or contact Marnie at 6031 2946</p>
  </div>
</div>
</body>
</html>
```